Gaming Developer Wordpress Website

I am looking for someone to design a standout website for my video game developer website. We are currently developing a strategy / sim game.
Id like the following pages:
1) Games (will have a picture icon of games that we release, gamers can click each to take them to another page specifically about that game)
2) News (this will host news on coming soon or released games and general content updates)
3) Videos (this might host videos on my games or link to my ClipVane account)
4) Company (general about, mission, vison, and other info on the team and founder)
5) Support (a form gamers can fill out for help)
Id like the ability for gamers to create an account and sign up for my company newsletter.
At some point I want to be able to add a forum to my site to drive further traffic and allow gamers to discuss my games, so please make sure this is possible.
Design and color wise:
I would like the background to be a dark color, preferably black or maybe grey. I am looking for something clean, and that properly fits the gaming space.
(Lastly, I own the domain for my site, and it is currently hosted on wordpress).

```html
<!DOCTYPE html>
<html lang="en">
<head>
<meta charset="utf-8">
<title>905 Interactive</title>
<link href="https://fonts.googleapis.com/css2?family=Orbitron:wght@600;800&family=PT+Sans:wght@400;700&family=PT+Sans+Narrow:wght@400;700&display=swap" rel="stylesheet">
<style>
:root{
  --ink:#0b0e12;
  --panel:#07090c;
  --steel:#8fa8b8;
  --steel-dark:#6f8a9c;
  --nav:#c6c8ca;
  --white:#ffffff;
  --text:#e8ecef;
  --muted:#b8c0c6;
  --line:#4a5560;
  --red:#d3202a;
}
*{box-sizing:border-box;margin:0;padding:0}
html,body{width:1200px;height:2642px;overflow:hidden;background:var(--ink)}
body{position:relative;font-family:"PT Sans",sans-serif;color:var(--text)}
.abs{position:absolute}
.display{font-family:"Orbitron",sans-serif;font-weight:800;letter-spacing:2px}
.narrow{font-family:"PT Sans Narrow",sans-serif;font-weight:700}

/* hero */
.hero{left:0;top:0;width:1200px;height:740px;background:radial-gradient(ellipse at 50% 30%,#7f9a98 0%,#4d6466 30%,#2b3a3e 60%,#0e1416 100%)}
.hero-fade{left:0;top:640px;width:1200px;height:120px;background:linear-gradient(180deg,rgba(11,14,18,0),var(--ink))}
.logo{left:166px;top:29px;width:136px;height:120px;background:#c9cbcc;padding:7px}
.logo-inner{width:100%;height:100%;background:#111;border:2px solid #aaa;display:flex;flex-direction:column;align-items:center;justify-content:center;color:var(--white);font-family:"PT Sans Narrow",sans-serif;font-weight:700;font-size:44px;line-height:1}
.logo-inner small{font-size:15px;letter-spacing:1px;margin-top:8px}
.nav{left:303px;top:48px;width:731px;height:80px;background:var(--nav);display:flex;align-items:center;padding-left:59px}
.nav a{font-family:"PT Sans Narrow",sans-serif;font-weight:700;font-size:16px;color:#111;text-decoration:none;margin-right:31px}
.nav a.active{background:var(--white);padding:29px 12px;margin-right:20px}
.nav .user{width:22px;height:22px;border:2px solid #111;border-radius:50%;margin-left:0;margin-right:24px}
.nav .signup{background:var(--steel-dark);border:1px solid #556;color:var(--white);font-family:"PT Sans Narrow",sans-serif;font-weight:700;font-size:14px;padding:9px 13px}
.hero-title{left:0;top:268px;width:1200px;text-align:center;font-size:70px;color:var(--white)}
.hero-sub{left:0;top:369px;width:1200px;text-align:center;font-weight:700;font-size:20px;line-height:23px}
.hero-btn{left:525px;top:440px;width:151px;height:44px;background:var(--steel);border:1px solid #aab;color:var(--white);font-family:"PT Sans Narrow",sans-serif;font-weight:700;font-size:16px;display:flex;align-items:center;justify-content:center}
.dots{left:565px;top:592px;display:flex;gap:14px;align-items:center}
.dots span{width:10px;height:10px;border-radius:50%;background:#999}
.dots span.on{width:16px;height:16px;background:#ccc;border:3px solid #777}

/* body grid backdrop */
.stage{left:0;top:740px;width:1200px;height:1545px;background:linear-gradient(180deg,#123038 0%,#0c1318 20%,#0b0e12 60%,#101a22 100%)}
.sec-title{font-size:38px;color:var(--white)}
.arrows{display:flex;gap:6px}
.arrows span{width:27px;height:27px;border:2px solid #ccc;border-radius:50%;display:flex;align-items:center;justify-content:center;color:#ddd;font-size:14px}
.box{border:1px solid #6a737c;background:var(--panel)}
.thumb{display:block}
.tab{background:var(--steel);color:var(--white);font-family:"Orbitron",sans-serif;font-weight:800;font-size:21px;letter-spacing:1px;display:flex;align-items:center;justify-content:center}
.game-label{font-family:"PT Sans Narrow",sans-serif;font-weight:700;font-size:15px;text-align:center;width:183px}
.badge{background:var(--red);color:var(--white);font-size:11px;font-weight:700;padding:2px 7px}
.news-card{width:287px}
.news-card h3{font-family:"PT Sans Narrow",sans-serif;font-weight:700;font-size:15px;line-height:21px;margin-top:28px;color:var(--white)}
.news-card .date{font-size:12px;margin-top:10px;color:var(--muted);display:flex;gap:8px;align-items:center}
.news-card .date i{width:11px;height:11px;background:var(--muted);display:inline-block}
.news-card p{font-size:12px;line-height:18px;margin-top:13px;color:var(--muted)}
.more{font-family:"PT Sans Narrow",sans-serif;font-weight:700;font-size:15px;color:var(--white);text-decoration:underline;display:inline-block;margin-top:13px}
.play{position:absolute;left:50%;top:50%;width:40px;height:40px;margin:-20px 0 0 -20px;border-radius:50%;background:var(--white)}
.play:after{content:"";position:absolute;left:15px;top:11px;border-left:14px solid #111;border-top:9px solid transparent;border-bottom:9px solid transparent}
.forum-item{left:815px;width:230px}
.avatar{width:44px;height:44px;border-radius:50%;background:#c9cbcc}
.forum-name{font-family:"PT Sans Narrow",sans-serif;font-weight:700;font-size:16px;line-height:22px}
.forum-stats{font-size:10px;line-height:15px;font-weight:700}
.forum-text{font-size:12px;line-height:18px;color:var(--muted)}

/* newsletter */
.newsletter{left:0;top:2285px;width:1200px;height:142px;background:var(--steel)}
.nl-title{left:143px;top:2311px;font-size:36px;line-height:46px;color:var(--white)}
.nl-input{left:592px;top:2335px;width:303px;height:43px;background:var(--white);border:1px solid #777;color:#333;font-size:13px;padding:13px 23px}
.nl-btn{left:904px;top:2335px;width:151px;height:43px;background:#000;color:var(--white);font-family:"PT Sans Narrow",sans-serif;font-weight:700;font-size:16px;display:flex;align-items:center;justify-content:center}

/* footer */
.footer{left:0;top:2427px;width:1200px;height:215px;background:linear-gradient(180deg,#0b0e12 0%,#1a1f35 55%,#123a3c 100%)}
.foot-nav{left:143px;top:2480px;display:flex;gap:31px}
.foot-nav a{font-family:"PT Sans Narrow",sans-serif;font-weight:700;font-size:15px;color:var(--white);text-decoration:none}
.legal{left:143px;top:2523px;font-size:14px;color:var(--white)}
.social{left:822px;top:2489px;display:flex;gap:8px}
.social span{display:flex;align-items:center;gap:3px;font-size:11px;font-weight:700;color:var(--white)}
.social span i{width:12px;height:12px;border-radius:50%;background:var(--white);display:inline-block}
</style>
</head>
<body>

<!-- Hero -->
<div class="abs hero" role="img" aria-label="Sci-fi scene of an armoured explorer standing among ruined industrial structures in teal haze"></div>
<div class="abs hero-fade"></div>
<div class="abs logo"><div class="logo-inner">905<small>INTERACTIVE</small></div></div>
<nav class="abs nav">
  <a class="active" href="#">HOME</a><a href="#">GAMES</a><a href="#">NEWS</a><a href="#">VIDEOS</a><a href="#">COMPANY</a><a href="#">SUPPORT</a>
  <span class="user"></span><span class="signup">&#9998; SIGN UP</span>
</nav>
<h1 class="abs hero-title display">905 INTERACTIVE</h1>
<p class="abs hero-sub">Lorem ipsum dolor sit amet, consectetur adipiscing eli<br>sed do eiusmod temp</p>
<div class="abs hero-btn">GET STARTED</div>
<div class="abs dots"><span></span><span class="on"></span><span></span></div>

<!-- Content stage -->
<div class="abs stage" role="img" aria-label="Dark backdrop with glowing purple and teal perspective grid lines"></div>

<!-- Featured games -->
<h2 class="abs sec-title display" style="left:145px;top:752px">FEATURED GAMES</h2>
<div class="abs arrows" style="left:709px;top:761px"><span>&larr;</span><span>&rarr;</span></div>
<div class="abs box" style="left:147px;top:831px;width:623px;height:302px"></div>
<div class="abs thumb" style="left:161px;top:849px;width:183px;height:226px;background:linear-gradient(135deg,#0e6a55,#1aa79a,#0b2b33)" role="img" aria-label="Cybernetic android character in green neon light"></div>
<div class="abs thumb" style="left:366px;top:848px;width:185px;height:228px;border:1px solid #ccc;background:linear-gradient(180deg,#6f8fc4,#3c4d7a,#15192a)" role="img" aria-label="Giant robot towering over a city skyline at dusk"></div>
<span class="abs badge" style="left:501px;top:862px">TOP</span>
<div class="abs thumb" style="left:573px;top:849px;width:183px;height:226px;background:linear-gradient(160deg,#c6792e,#8d4a3a,#3d2c4a)" role="img" aria-label="Astronaut in orange suit facing an alien creature among glowing particles"></div>
<div class="abs game-label" style="left:161px;top:1087px">BORIS NLIQUIP</div>
<div class="abs game-label" style="left:367px;top:1087px">BORIS NLIQUIP</div>
<div class="abs game-label" style="left:573px;top:1087px">BORIS NLIQUIP</div>

<!-- Company -->
<div class="abs box" style="left:793px;top:777px;width:263px;height:356px"></div>
<div class="abs tab" style="left:815px;top:760px;width:219px;height:40px">COMPANY</div>
<p class="abs" style="left:820px;top:824px;width:210px;font-size:12px;line-height:20px;text-align:justify;text-align-last:center">Sed ut perspiciatis unde omnis iste natus error sit voluptatem accusantium doloremque laudantium, totam rem aperiam, eaque ipsa quae ab illo inventore veritatis et quasi</p>
<a class="abs more" style="left:892px;top:920px;font-size:12px;margin:0">READ MORE</a>
<div class="abs thumb" style="left:794px;top:950px;width:261px;height:182px;background:linear-gradient(120deg,#0b1a44,#233e7a,#5a2a3e)" role="img" aria-label="Developer wearing a headset working at a lit keyboard"></div>

<!-- Latest news -->
<h2 class="abs sec-title display" style="left:145px;top:1169px">LATEST NEWS</h2>
<div class="abs arrows" style="left:709px;top:1178px"><span>&larr;</span><span>&rarr;</span></div>
<div class="abs box" style="left:147px;top:1249px;width:623px;height:976px"></div>

<div class="abs news-card" style="left:163px;top:1275px">
  <div class="thumb" style="height:225px;background:linear-gradient(135deg,#0d2a5e,#2a71c4,#0a1630)" role="img" aria-label="Player holding a controller in front of a racing game on screen"></div>
  <h3>EOMNIS ISTE NATUS ERROE OMNIS<br>ISTE NATUS ERRO</h3>
  <div class="date"><i></i>October 04,2024</div>
  <p>Sed ut perspiciatis unde omnis iste natus error sit voluptatem accusantium doloremque laudantium, totam rem aperiam</p>
  <a class="more">READ MORE</a>
</div>
<div class="abs news-card" style="left:466px;top:1275px">
  <div class="thumb" style="height:225px;background:linear-gradient(160deg,#2a2f3c,#4a4f5e,#141821)" role="img" aria-label="Armoured warrior in a dark industrial hall"></div>
  <h3>EOMNIS ISTE NATUS ERROE OMNIS<br>ISTE NATUS ERRO</h3>
  <div class="date"><i></i>October 04,2024</div>
  <p>Sed ut perspiciatis unde omnis iste natus error sit voluptatem accusantium doloremque laudantium, totam rem aperiam</p>
  <a class="more">READ MORE</a>
</div>
<div class="abs news-card" style="left:163px;top:1750px">
  <div class="thumb" style="height:225px;background:linear-gradient(160deg,#6b2a24,#3b2a2e,#1a1418)" role="img" aria-label="Figure in red coat walking through a ruined red-lit factory"></div>
  <h3>EOMNIS ISTE NATUS ERROE OMNIS<br>ISTE NATUS ERRO</h3>
  <div class="date"><i></i>October 04,2024</div>
  <p>Sed ut perspiciatis unde omnis iste natus error sit voluptatem accusantium doloremque laudantium, totam rem aperiam</p>
  <a class="more">READ MORE</a>
</div>
<div class="abs news-card" style="left:466px;top:1750px">
  <div class="thumb" style="height:225px;background:radial-gradient(ellipse at 50% 60%,#1f55c9,#0b2a7a 55%,#050f33)" role="img" aria-label="Holographic blue car on a digital grid dashboard"></div>
  <h3>EOMNIS ISTE NATUS ERROE OMNIS<br>ISTE NATUS ERRO</h3>
  <div class="date"><i></i>October 04,2024</div>
  <p>Sed ut perspiciatis unde omnis iste natus error sit voluptatem accusantium doloremque laudantium, totam rem aperiam</p>
  <a class="more">READ MORE</a>
</div>
<span class="abs" style="left:624px;top:1767px;background:var(--white);color:#111;font-family:'Orbitron',sans-serif;font-weight:600;font-size:11px;padding:6px 10px">COMING SOON</span>

<!-- Videos -->
<div class="abs box" style="left:793px;top:1194px;width:263px;height:547px"></div>
<div class="abs tab" style="left:815px;top:1177px;width:219px;height:40px">VIDEOS</div>
<div class="abs" style="left:815px;top:1232px;width:219px;height:145px;background:linear-gradient(140deg,#8a7a62,#4d4536,#1e1c18)" role="img" aria-label="Battle scene with a giant creature"><span class="play"></span></div>
<div class="abs" style="left:815px;top:1386px;width:219px;height:145px;background:linear-gradient(140deg,#1a5a8f,#0f2f55,#07142a)" role="img" aria-label="Armoured soldier in blue light"><span class="play"></span></div>
<div class="abs" style="left:815px;top:1540px;width:219px;height:145px;border:2px solid var(--red);background:radial-gradient(circle at 50% 50%,#6a6d76,#2c2f38 60%,#121419)" role="img" aria-label="Space trooper in red armour inside a tunnel"><span class="play"></span></div>
<span class="abs" style="left:974px;top:1650px;font-size:11px;font-weight:700;color:var(--white)">ClipVane</span>
<a class="abs more" style="left:884px;top:1700px;margin:0">LOAD MORE</a>

<!-- Forum -->
<div class="abs box" style="left:793px;top:1811px;width:263px;height:414px"></div>
<div class="abs tab" style="left:815px;top:1795px;width:219px;height:41px">FORUM LIST</div>
<div class="abs forum-item" style="top:1865px">
  <div style="display:flex;gap:14px;align-items:flex-start">
    <div class="avatar"></div>
    <div class="forum-name" style="width:110px">EOMNIS ISIS<br>ISTE NATU</div>
    <div class="forum-stats">&#9673; 223<br>&#9719; 23</div>
  </div>
  <p class="forum-text" style="margin-top:14px">Sed ut perspiciatis unde omnis iste<br>natus error sit voluptatem</p>
</div>
<div class="abs" style="left:803px;top:1984px;width:243px;border-top:1px solid var(--line)"></div>
<div class="abs forum-item" style="top:2002px">
  <div style="display:flex;gap:14px;align-items:flex-start">
    <div class="avatar"></div>
    <div class="forum-name" style="width:110px">EOMNIS ISIS<br>ISTE NATU</div>
    <div class="forum-stats">&#9673; 223<br>&#9719; 23</div>
  </div>
  <p class="forum-text" style="margin-top:14px">Sed ut perspiciatis unde omnis iste<br>natus error sit voluptatem</p>
</div>
<div class="abs" style="left:803px;top:2121px;width:243px;border-top:1px solid var(--line)"></div>
<div class="abs hero-btn" style="left:850px;top:2146px;width:150px;height:43px;border:none">VIEW MORE</div>

<!-- Newsletter -->
<div class="abs newsletter"></div>
<h2 class="abs nl-title display">SIGN UP TO<br>OUR NEWSLETTER</h2>
<div class="abs nl-input">Enter Email</div>
<div class="abs nl-btn">SIGN UP</div>

<!-- Footer -->
<footer class="abs footer" role="img" aria-label="Dark footer backdrop with purple and teal perspective grid glow"></footer>
<nav class="abs foot-nav"><a href="#">HOME</a><a href="#">GAMES</a><a href="#">NEWS</a><a href="#">VIDEOS</a><a href="#">COMPANY</a><a href="#">SUPPORT</a></nav>
<p class="abs legal">&copy; 905 Interactive.All Rights Reserved &nbsp;|&nbsp; Privacy Policy &nbsp;|&nbsp; Terms of use</p>
<div class="abs social">
  <span><i></i>Lumo</span><span><i></i>Kinly</span><span><i></i>Zeet</span><span><i></i>ClipVane</span><span><i></i>Linko</span>
</div>

</body>
</html>
```